Women's Health Company needs business card

We need a business card for a USA based women's health care company. We use digital technology to enhance therapy prescribed by clinicians for their patients

```html
<!DOCTYPE html>
<html lang="en">
<head>
<meta charset="utf-8">
<title>Velora Health – Business Card</title>
<link href="https://fonts.googleapis.com/css2?family=Lato:wght@300;400;700&display=swap" rel="stylesheet">
<style>
  :root {
    --page-bg: #ecebef;
    --purple: #9a53b8;
    --purple-light: #b676cf;
    --purple-dark: #7c3b99;
    --teal: #a9ddd7;
    --ink: #2b2b2e;
    --muted: #4a4a50;
    --card-white: #ffffff;
  }
  * { box-sizing: border-box; margin: 0; padding: 0; }
  html, body {
    width: 1200px; height: 1023px; overflow: hidden;
    background: var(--page-bg);
    font-family: "Lato", Arial, sans-serif;
  }
  .sheet {
    width: 1200px; height: 1023px;
    display: flex; flex-direction: column;
    align-items: center; justify-content: center; gap: 60px;
  }
  .card {
    width: 660px; height: 377px;
    border-radius: 6px;
    box-shadow: 0 10px 28px rgba(0,0,0,.18);
    position: relative; overflow: hidden;
  }
  /* Front */
  .card-front {
    background: linear-gradient(135deg, var(--purple-dark) 0%, var(--purple-light) 50%, var(--purple) 100%);
    display: flex; align-items: center; justify-content: center;
  }
  .brand {
    display: flex; align-items: center; gap: 14px;
    font-weight: 300; color: var(--teal);
  }
  .brand-dot {
    width: 14px; height: 14px; border-radius: 50%; background: var(--teal);
  }
  .card-front .brand-name { font-size: 58px; letter-spacing: 2px; }
  /* Back */
  .card-back {
    background: var(--card-white);
    padding: 48px 52px;
    display: grid; grid-template-columns: 1fr 1fr; column-gap: 40px;
  }
  .person-name { font-size: 22px; font-weight: 700; color: var(--ink); letter-spacing: .5px; }
  .person-title { font-size: 15px; font-weight: 300; color: var(--purple-light); margin-top: 4px; }
  .contact-list { list-style: none; margin-top: 44px; }
  .contact-item {
    display: flex; align-items: flex-start; gap: 14px;
    font-size: 13px; color: var(--muted); line-height: 1.5; margin-bottom: 18px;
  }
  .icon {
    flex: none; width: 28px; height: 28px; border-radius: 50%;
    background: var(--purple);
    display: flex; align-items: center; justify-content: center;
  }
  .icon svg { width: 15px; height: 15px; fill: #fff; }
  .side-right { display: flex; flex-direction: column; justify-content: space-between; }
  .card-back .brand { align-self: flex-end; margin-top: 60px; }
  .card-back .brand-name { font-size: 34px; letter-spacing: 1px; }
  .card-back .brand-dot { width: 9px; height: 9px; }
  .card-back .contact-list { margin-top: 0; }
</style>
</head>
<body>
<main class="sheet">
  <section class="card card-front" aria-label="Card front">
    <div class="brand">
      <span class="brand-dot"></span>
      <span class="brand-name">Velora Health</span>
    </div>
  </section>

  <section class="card card-back" aria-label="Card back">
    <div class="side-left">
      <h1 class="person-name">YOUR NAME HERE</h1>
      <p class="person-title">Managing Director</p>
      <ul class="contact-list">
        <li class="contact-item">
          <span class="icon"><svg viewBox="0 0 24 24"><path d="M6.6 10.8a15.1 15.1 0 0 0 6.6 6.6l2.2-2.2a1 1 0 0 1 1-.25 11.4 11.4 0 0 0 3.6.57 1 1 0 0 1 1 1V20a1 1 0 0 1-1 1A17 17 0 0 1 3 4a1 1 0 0 1 1-1h3.5a1 1 0 0 1 1 1c0 1.25.2 2.45.57 3.57a1 1 0 0 1-.25 1z"/></svg></span>
          <span>+1 555 014 2281<br>+1 555 019 6630</span>
        </li>
        <li class="contact-item">
          <span class="icon"><svg viewBox="0 0 24 24"><path d="M12 2a10 10 0 1 0 0 20 10 10 0 0 0 0-20zm6.9 6h-3a15.6 15.6 0 0 0-1.4-3.6A8 8 0 0 1 18.9 8zM12 4c.8 1.2 1.5 2.5 1.9 4h-3.8c.4-1.5 1.1-2.8 1.9-4zM4.3 14a8 8 0 0 1 0-4h3.4a16 16 0 0 0 0 4zm.8 2h3a15.6 15.6 0 0 0 1.4 3.6A8 8 0 0 1 5.1 16zm3-8h-3a8 8 0 0 1 4.4-3.6C8.9 5.5 8.4 6.7 8.1 8zM12 20c-.8-1.2-1.5-2.5-1.9-4h3.8c-.4 1.5-1.1 2.8-1.9 4zm2.3-6H9.7a14.7 14.7 0 0 1 0-4h4.6a14.7 14.7 0 0 1 0 4zm.3 5.6c.6-1.1 1.1-2.3 1.4-3.6h3a8 8 0 0 1-4.4 3.6zm1.7-5.6a16 16 0 0 0 0-4h3.4a8 8 0 0 1 0 4z"/></svg></span>
          <span>www.velorahealth.example</span>
        </li>
      </ul>
    </div>
    <div class="side-right">
      <div class="brand">
        <span class="brand-dot"></span>
        <span class="brand-name">Velora Health</span>
      </div>
      <ul class="contact-list">
        <li class="contact-item">
          <span class="icon"><svg viewBox="0 0 24 24"><path d="M12 3 2 12h3v8h5v-5h4v5h5v-8h3z"/></svg></span>
          <span>12 Harbor Lane<br>Brookfield, 0421</span>
        </li>
        <li class="contact-item">
          <span class="icon"><svg viewBox="0 0 24 24"><path d="M2 11 22 3l-6 18-4-7z"/></svg></span>
          <span>hello@velorahealth.example</span>
        </li>
      </ul>
    </div>
  </section>
</main>
</body>
</html>
```